QuillMark Business Cards

I need a business card designed for QuillMark. To get an idea of what we do please visit https://formvault.example/para-creadores-3

```html
<!DOCTYPE html>
<html lang="en">
<head>
<meta charset="utf-8">
<title>QuillMark Business Cards</title>
<link rel="stylesheet" href="https://fonts.googleapis.com/css2?family=Josefin+Sans:wght@300;400&family=Open+Sans:wght@400&display=swap">
<style>
  :root {
    --backdrop: #e9e9e9;
    --paper: #fbfbfa;
    --ink: #232222;
    --ink-soft: #2e2d2d;
    --band: #3a3939;
    --orange: #f2931c;
    --white: #ffffff;
    --rule: #9a9a9a;
  }
  * { box-sizing: border-box; margin: 0; padding: 0; }
  html, body {
    width: 1200px; height: 1200px; overflow: hidden;
    background: var(--backdrop);
  }
  .canvas {
    width: 1200px; height: 1200px;
    display: flex; flex-direction: column; align-items: center; justify-content: center;
    gap: 70px;
  }
  .card {
    width: 860px; height: 491px;
    position: relative; overflow: hidden;
    box-shadow: 0 6px 18px rgba(0,0,0,0.12);
  }

  /* Front */
  .card-front { background: var(--paper); }
  .front-brand {
    position: absolute; left: 0; right: 0; top: 0; height: 344px;
    display: flex; flex-direction: column; align-items: center; justify-content: center;
    gap: 26px;
  }
  .brand-dot {
    width: 46px; height: 46px; border-radius: 50%;
    border: 3px solid var(--orange);
  }
  .front-name {
    font-family: "Josefin Sans", sans-serif; font-weight: 400;
    font-size: 34px; letter-spacing: 6px; color: var(--ink);
    text-transform: uppercase;
  }
  .front-band {
    position: absolute; left: 0; right: 0; bottom: 0; height: 147px;
    background: var(--ink);
    display: flex; align-items: center; justify-content: center;
  }
  .front-tagline {
    font-family: "Josefin Sans", sans-serif; font-weight: 400;
    font-size: 26px; letter-spacing: 9px; color: var(--orange);
  }

  /* Back */
  .card-back { background: var(--ink); display: flex; }
  .back-brand {
    width: 410px; height: 100%; background: var(--paper);
    display: flex; flex-direction: column; justify-content: center;
    padding-left: 70px;
  }
  .back-name {
    font-family: "Josefin Sans", sans-serif; font-weight: 400;
    font-size: 32px; letter-spacing: 5px; color: var(--ink);
    text-transform: uppercase;
  }
  .back-tagline-row { display: flex; align-items: center; gap: 10px; margin-top: 6px; }
  .back-tagline {
    font-family: "Josefin Sans", sans-serif; font-weight: 400;
    font-size: 11px; letter-spacing: 3px; color: var(--orange);
  }
  .back-rule { width: 110px; height: 1px; background: var(--rule); }
  .accent-stripe { width: 9px; height: 100%; background: var(--orange); }
  .contact-list {
    position: absolute; left: 0; right: 0; top: 0; bottom: 0;
    display: flex; flex-direction: column; justify-content: center; gap: 22px;
  }
  .contact-row {
    position: relative; height: 88px;
    display: flex; align-items: center;
  }
  .contact-row.is-highlight::before {
    content: ""; position: absolute; left: 419px; right: 0; top: 0; bottom: 0;
    background: var(--band);
  }
  .contact-icon {
    position: absolute; left: 384px; top: 50%; transform: translateY(-50%);
    width: 48px; height: 48px; border-radius: 50%;
    background: var(--orange);
    display: flex; align-items: center; justify-content: center;
  }
  .contact-icon svg { width: 26px; height: 26px; }
  .contact-text {
    position: relative; margin-left: 480px;
    font-family: "Open Sans", sans-serif; font-size: 24px; line-height: 1.3;
    color: var(--white);
  }
</style>
</head>
<body>
<main class="canvas">

  <section class="card card-front" aria-label="Business card front">
    <div class="front-brand">
      <span class="brand-dot"></span>
      <h1 class="front-name">QuillMark</h1>
    </div>
    <div class="front-band">
      <p class="front-tagline">DIGITAL NOTARY</p>
    </div>
  </section>

  <section class="card card-back" aria-label="Business card back">
    <div class="back-brand">
      <h2 class="back-name">QuillMark</h2>
      <div class="back-tagline-row">
        <span class="back-tagline">DIGITAL NOTARY</span>
        <span class="back-rule"></span>
      </div>
    </div>
    <div class="accent-stripe"></div>

    <div class="contact-list">
      <div class="contact-row">
        <span class="contact-icon">
          <svg viewBox="0 0 24 24" fill="none" stroke="#fff" stroke-width="2" stroke-linejoin="round">
            <path d="M5 8c0-2 2-3 7-3s7 1 7 3l-2 1.5-2-1V7H9v1.5L7 9.5z" fill="#fff"/>
            <rect x="6" y="11" width="12" height="8" rx="1.5" fill="#fff"/>
          </svg>
        </span>
        <p class="contact-text">+000 12345 6789<br>+000 12345 6789</p>
      </div>
      <div class="contact-row is-highlight">
        <span class="contact-icon">
          <svg viewBox="0 0 24 24" fill="none" stroke="#fff" stroke-width="1.8">
            <circle cx="12" cy="12" r="8.5"/>
            <ellipse cx="12" cy="12" rx="3.8" ry="8.5"/>
            <path d="M3.5 12h17M5 7.5h14M5 16.5h14"/>
          </svg>
        </span>
        <p class="contact-text">urwebsitename.com<br>urname@email.com</p>
      </div>
      <div class="contact-row">
        <span class="contact-icon">
          <svg viewBox="0 0 24 24">
            <path d="M12 2.5a6.5 6.5 0 0 0-6.5 6.5c0 5 6.5 12.5 6.5 12.5S18.5 14 18.5 9A6.5 6.5 0 0 0 12 2.5z" fill="#fff"/>
            <circle cx="12" cy="9" r="2.6" fill="#f2931c"/>
          </svg>
        </span>
        <p class="contact-text">Street Address Here<br>Singapore, 2222</p>
      </div>
    </div>
  </section>

</main>
</body>
</html>
```